Lanterns Harvest Night flyer design contest

Name of event: Lantern’s Harvest Night

Tagline: ‘While the Queen’s away the staff will play’

Description: ‘…while the Queen is out celebrating her birthday with high tea, the palace staff are throwing a party at 14th loftspace and drinking her booze!

Date: Sunday 10th June 2012

Time: 8pm-3am

Dress code: Smart/casual or join in the theme

TICKETS
-Purchased through our website or Chatterly page, at the venue or at the door

Pre-Purchase Tickets: $10

Entry on the night (subject to availability): $15

Tickets Include:

Priority entry
Finger food from 9-10pm
‘Kir Royal’ cocktail on arrival

DRINK SPECIALS

$10 Kir Royal’s all night long!
$20 Valdoro buckets from 9-11pm

DJ's

Playing from 9-3am

Line up includes:

Dusky Amber
Tilted
DJ Marvek

Ph: (03) 9514 2760
Web: www.14thloftspace.com.au
Address: 14 Marlowe Lane St Kilda

I have attached an image which shows the feel that I am going for (plz see att.)

Reason: I wanted a 3 day deadline but this option was not available on the booking screen

Hi there,

If anyone finds a stock image that is appropriate you can add the low res to the mock up and if your design wins i can purchase the image to replace it (up to $20).. hope this helps :) Lira

Target Market(s)

Target Market is 20-35 year olds

Industry/Entity Type

Apartment

Requirements
Must have
• Must have a graphical/picture element to it
Also must have our company logo
Must have all the information listed in the task description
Must be a fun and cool design

```html
<!DOCTYPE html>
<html lang="en">
<head>
<meta charset="utf-8">
<title>Lantern’s Harvest Night</title>
<link rel="stylesheet" href="https://fonts.googleapis.com/css2?family=Great+Vibes&family=Arimo:wght@400;700&family=Roboto+Condensed:wght@400;700&display=swap">
<style>
  :root {
    --plum-deep: #2e2550;
    --plum: #5a4f8a;
    --lavender: #a99fd6;
    --mist: #e9e6f3;
    --paper: #ffffff;
    --ink: #111111;
    --ink-navy: #2b2a4a;
    --dot: #333333;
  }
  * { margin: 0; padding: 0; box-sizing: border-box; }
  html, body { width: 848px; height: 1200px; overflow: hidden; background: var(--paper); }
  .flyer {
    position: relative;
    width: 848px;
    height: 1200px;
    overflow: hidden;
    font-family: "Arimo", Arial, sans-serif;
    color: var(--ink);
    background:
      radial-gradient(ellipse 70% 55% at 62% 78%, rgba(255,255,255,0.95) 0%, rgba(255,255,255,0.6) 40%, rgba(255,255,255,0) 75%),
      linear-gradient(180deg, var(--plum-deep) 0%, var(--plum) 28%, #8d85b4 44%, var(--mist) 62%, var(--paper) 100%);
  }
  .flyer__rays {
    position: absolute;
    inset: 0;
    background:
      repeating-conic-gradient(from 200deg at 62% 82%, rgba(255,255,255,0.10) 0deg 4deg, rgba(255,255,255,0) 4deg 11deg);
    -webkit-mask-image: linear-gradient(180deg, rgba(0,0,0,0.9) 0%, rgba(0,0,0,0.6) 60%, rgba(0,0,0,0.2) 100%);
            mask-image: linear-gradient(180deg, rgba(0,0,0,0.9) 0%, rgba(0,0,0,0.6) 60%, rgba(0,0,0,0.2) 100%);
  }
  .title {
    position: absolute;
    left: 0; top: 70px; width: 100%;
    font-family: "Great Vibes", cursive;
    color: var(--paper);
    font-weight: 400;
    text-shadow: 0 2px 6px rgba(0,0,0,0.35);
  }
  .title__line1 { position: absolute; left: 136px; top: 0; font-size: 146px; line-height: 1; }
  .title__line2 { position: absolute; left: 246px; top: 126px; font-size: 124px; line-height: 1; }
  .title__accent { position: absolute; left: 628px; top: 204px; font-size: 62px; line-height: 1; color: var(--lavender); }
  .tagline {
    position: absolute; left: 0; top: 366px; width: 100%;
    text-align: center; color: var(--paper);
    font-size: 26px; font-weight: 700;
  }
  .intro {
    position: absolute; left: 56px; top: 412px; width: 736px;
    text-align: center; color: var(--paper);
    font-size: 19.5px; line-height: 28px;
  }
  .divider {
    position: absolute; left: 12px; width: 824px; height: 7px;
    background: repeating-linear-gradient(90deg, var(--dot) 0 7px, transparent 7px 17.6px);
  }
  .divider--top { top: 510px; }
  .divider--bottom { top: 621px; }
  .details {
    position: absolute; left: 0; top: 536px; width: 100%;
    text-align: center;
    font-family: "Roboto Condensed", "Arial Narrow", sans-serif;
    font-size: 31px; line-height: 37px; color: var(--ink);
  }
  .details b { font-weight: 700; }
  .section-title {
    font-family: "Roboto Condensed", "Arial Narrow", sans-serif;
    font-weight: 700; color: var(--ink-navy);
    font-size: 28px; letter-spacing: 0.5px;
  }
  .section-sub { font-weight: 700; color: var(--ink-navy); font-size: 20px; }
  .copy { font-size: 17px; line-height: 20px; color: var(--ink); }
  .tickets { position: absolute; left: 78px; top: 680px; width: 420px; }
  .tickets .copy { margin-top: 6px; }
  .tickets .copy + .copy { margin-top: 12px; }
  .tickets .section-sub { margin-top: 18px; }
  .tickets__list { list-style: none; margin-top: 6px; }
  .drinks { position: absolute; left: 78px; top: 956px; width: 420px; }
  .drinks .copy { margin-top: 6px; }
  .djs { position: absolute; left: 594px; top: 680px; width: 230px; }
  .djs .copy { margin-top: 6px; }
  .djs__lineup { list-style: none; margin-top: 16px; margin-left: 14px; font-size: 21px; line-height: 27px; }
  .brand {
    position: absolute; left: 432px; top: 1028px;
    display: flex; align-items: center; gap: 12px;
  }
  .brand__name {
    font-family: "Arimo", Arial, sans-serif; font-weight: 700;
    font-size: 44px; color: var(--ink); letter-spacing: -0.5px;
  }
  .brand__dot { width: 22px; height: 22px; border-radius: 50%; background: var(--ink); }
  .contact {
    position: absolute; right: 50px; top: 1090px;
    text-align: right; font-size: 16.5px; line-height: 23px; color: var(--ink);
    font-style: normal;
  }
  .contact b { font-weight: 700; }
</style>
</head>
<body>
<main class="flyer">
  <div class="flyer__rays"></div>

  <h1 class="title">
    <span class="title__line1">Lantern’s</span>
    <span class="title__line2">Harvest</span>
    <span class="title__accent">Night</span>
  </h1>

  <p class="tagline">While the Queen’s away the staff will play</p>
  <p class="intro">…while the Queen is out celebrating her birthday with high tea, the palace staff are throwing a party at 14th loftspace and drinking her booze!</p>

  <div class="divider divider--top"></div>
  <div class="details">
    <p><b>DATE:</b> SUNDAY 10TH JUNE 2012 - <b>TIME:</b> 8PM-3AM</p>
    <p><b>DRESS CODE:</b> SMART/CASUAL OR JOIN IN THE THEME</p>
  </div>
  <div class="divider divider--bottom"></div>

  <section class="tickets">
    <h2 class="section-title">TICKETS</h2>
    <p class="copy">Purchased through our website or<br>Chatterly page, at the venue or at the door</p>
    <p class="copy">Pre-Purchase Tickets: <b>$10</b><br>Entry on the night (subject to availability): <b>$15</b></p>
    <h3 class="section-sub">Tickets Include:</h3>
    <ul class="tickets__list copy">
      <li>Priority entry</li>
      <li>Finger food from 9-10pm</li>
      <li>‘Kir Royal’ cocktail on arrival</li>
    </ul>
  </section>

  <section class="drinks">
    <h2 class="section-title">DRINK SPECIALS</h2>
    <p class="copy"><b>$10</b> Kir Royal’s all night long!<br><b>$20</b> Valdoro buckets from 9-11pm</p>
  </section>

  <section class="djs">
    <h2 class="section-title">DJ's</h2>
    <p class="copy">Playing from 9-3am<br>Line up includes:</p>
    <ul class="djs__lineup">
      <li>Dusky Amber</li>
      <li>Tilted</li>
      <li>DJ Marvek</li>
    </ul>
  </section>

  <div class="brand">
    <span class="brand__name">14th loftspace</span>
    <span class="brand__dot"></span>
  </div>

  <address class="contact">
    <p><b>Ph:</b> (03) 9514 2760</p>
    <p><b>Web:</b> www.14thloftspace.com.au</p>
    <p><b>Address:</b> 14 Marlowe Lane St Kilda</p>
  </address>
</main>
</body>
</html>
```